Need a book cover design for book titled: Resting Beside the River--Simple Methods for the Crossing

This book describes and presents tools to connect with and activate the Lightbody that we all carry within us. It talks about the Lighbody, brief history, lightbody levels and offers exercises to bring light into the body.
I envision a design that shows a physical body changing into light /surrounded by light; a resurrected body ascending to higher dimensions of Spirit o anything comparable .
Updates

Target Market(s)

Mature audience of spiritual seekers and those on spiritual path

Requirements
Must have
• Space on backcover for book summary at top and title and author name on spine.

```html
<!DOCTYPE html>
<html lang="en">
<head>
<meta charset="utf-8">
<title>Resting Beside the River — Book Cover</title>
<link rel="stylesheet" href="https://fonts.googleapis.com/css2?family=Open+Sans:wght@300;400&family=Pinyon+Script&family=Josefin+Sans:wght@400&display=swap">
<style>
  :root {
    --night: #1d0d4a;
    --deep: #2b1468;
    --violet: #5b2d98;
    --orchid: #c27ad6;
    --blush: #f3b8e6;
    --glow: #fffaf4;
    --ember: #ef6a3a;
    --ink: #1c1240;
    --white: #ffffff;
  }
  html, body {
    margin: 0;
    padding: 0;
    width: 840px;
    height: 1200px;
    overflow: hidden;
    background: var(--night);
  }
  .cover {
    position: relative;
    width: 840px;
    height: 1200px;
    overflow: hidden;
  }
  .cover-art {
    position: absolute;
    inset: 0;
    background:
      radial-gradient(ellipse 150px 420px at 430px 760px, var(--glow) 0%, rgba(255,248,252,0.95) 35%, rgba(255,225,245,0.6) 65%, rgba(255,210,240,0) 100%),
      radial-gradient(ellipse 260px 300px at 430px 720px, rgba(255,255,255,0.9) 0%, rgba(250,200,240,0.55) 40%, rgba(220,150,230,0) 100%),
      radial-gradient(ellipse 460px 560px at 430px 740px, rgba(232,160,232,0.8) 0%, rgba(194,122,214,0.55) 40%, rgba(120,60,170,0.2) 75%, rgba(90,45,152,0) 100%),
      radial-gradient(ellipse 520px 200px at 430px 1200px, rgba(255,255,255,1) 0%, rgba(255,220,210,0.8) 30%, rgba(239,106,58,0.5) 65%, rgba(239,106,58,0) 100%),
      radial-gradient(ellipse 260px 340px at 40px 1040px, rgba(239,106,58,0.65) 0%, rgba(239,106,58,0) 100%),
      radial-gradient(ellipse 260px 340px at 820px 1040px, rgba(239,106,58,0.6) 0%, rgba(239,106,58,0) 100%),
      linear-gradient(180deg, var(--night) 0%, var(--deep) 25%, var(--violet) 55%, #7a3a98 78%, #b8587a 100%);
  }
  .title {
    position: absolute;
    left: 118px;
    top: 104px;
    margin: 0;
    color: var(--white);
    font-family: "Open Sans", sans-serif;
    font-weight: 400;
    line-height: 1;
  }
  .title-line {
    display: block;
    font-size: 88px;
    letter-spacing: -1px;
  }
  .title-line--second {
    margin-top: 6px;
  }
  .title-script {
    font-family: "Pinyon Script", cursive;
    font-size: 170px;
    margin-left: 6px;
    text-shadow: 3px 3px 0 var(--ink), 4px 4px 3px rgba(0,0,0,0.5);
    vertical-align: -38px;
    line-height: 0;
  }
  .subtitle {
    position: absolute;
    left: 0;
    right: 0;
    top: 406px;
    margin: 0;
    text-align: center;
    color: var(--white);
    font-family: "Open Sans", sans-serif;
    font-weight: 300;
    font-size: 27px;
    letter-spacing: 1.5px;
    text-transform: uppercase;
  }
  .author {
    position: absolute;
    left: 0;
    right: 0;
    top: 1110px;
    margin: 0;
    text-align: center;
    color: var(--ink);
    font-family: "Josefin Sans", sans-serif;
    font-size: 36px;
    letter-spacing: 6px;
    text-transform: uppercase;
  }
</style>
</head>
<body>
  <main class="cover">
    <div class="cover-art" role="img" aria-label="Radiant human silhouette dissolving into white light, with rays and sparkles bursting outward over a deep violet and orange cosmic background"></div>
    <h1 class="title">
      <span class="title-line">Resting Beside</span>
      <span class="title-line title-line--second">the<span class="title-script">River</span></span>
    </h1>
    <p class="subtitle">Simple Methods for the Crossing</p>
    <p class="author">Author Name</p>
  </main>
</body>
</html>
```